SCEN Banner Ad Design

We need a banner ad design for the Scholarly Capital Exchange Network (SCEN). SCEN is an internet-based consortium whose goal is to empower the global population to invest efficiently in financial markets by learning to apply a variety of quantitative stock market prediction techniques developed by professors at top U.S. universities. These techniques have good predictive performance for different classes of financial assets comparable to large existing mutual funds in the US. With the advent of online trading platforms, an increasing number of individual investors participate in the stock market. However, most individuals lack awareness about the existence of these academic prediction methods. Also, personalized decision-making based on these methods cannot be achieved without the application of optimal quantitative tools.
SCEN makes these prediction methods, and the tools for the optimal allocation of resources between different assets, freely available to the general public through a web platform that allows the user to a) learn about the extensive research at top U.S. universities that shows financial markets have a predictable component and identify models and asset classes that suit their investment preferences and objectives; b) back test these diverse trading models, using decades of historical stock market data, that provide returns in line with top investment houses and funds; c) obtain future predictions based on the underlying models; d) update the amounts invested in each of several assets at regular intervals of time according to the predictions of these models; e) track the performance of his portfolio in real time; f) build his financial social network whereby he can gain insights from other users as well as mirror their trading strategies in real time; and g) access leading financial experts from both academia and industry, who are available to provide advice and answer questions. All of the above features are novel additions to internet-based resources available to the average user.
The banner ad will be used on several websites, but first likely on CareerLoop (a social network for job searches) and CodeHarbor (an online community for software developers/engineers). The ad should capture the theme (and SCEN’s mission) of empowering the individual investor (along with the academic emphasis of the site) and leave a little room to be able to custom tailor it to a specific user demographic. For example, on CodeHarbor the goal is to target tech savvy individuals who undertake financial investments on their own, so we will need room on the ad itself to insert a “catch phrase” that speaks to these users specifically. Similarly, on CareerLoop, we may opt to target financial asset managers and so will insert a phrase into the ad that reaches out to these types of users. You can insert a few different phrases that you come up with on different versions of the ad intended for different groups of users. Here are also a few sample "catch phrases" for you to work with:
SCEN - Control Your Investments Without The Fees
SCEN – Beat the Market. Without The Fees.
SCEN – Hack the Markets. Without the Fees.
The SCEN Beta– Hack the Ivory Tower.
SCEN – Democratizing The Investment Landscape
Finally, we are open to different color schemes, but for reference the current version of the SCEN site uses a bluish theme.
Investment

```html
<!DOCTYPE html>
<html lang="en">
<head>
<meta charset="utf-8">
<title>SCEN Banner</title>
<link rel="stylesheet" href="https://fonts.googleapis.com/css2?family=Exo:wght@500;600&family=Open+Sans:wght@400;600;700;800&display=swap">
<style>
  :root {
    --page-bg: #aaaaaa;
    --panel-white: #f7f7f7;
    --panel-edge: #d9d9d9;
    --wordmark: #1c3f8f;
    --blue-deep: #2a3aa8;
    --blue-mid: #2f6ad0;
    --blue-light: #56b8ec;
    --tag-grey: #555555;
    --white: #ffffff;
  }
  * { margin: 0; padding: 0; box-sizing: border-box; }
  html, body {
    width: 1200px; height: 900px; overflow: hidden;
    background: var(--page-bg);
  }
  .banner {
    position: absolute;
    left: 54px; top: 382px;
    width: 1092px; height: 136px;
    overflow: hidden;
    border: 1px solid var(--panel-edge);
    background: linear-gradient(100deg, var(--blue-deep) 20%, var(--blue-mid) 62%, var(--blue-light) 100%);
  }
  .banner-bg { position: absolute; inset: 0; width: 100%; height: 100%; }
  .brand-name {
    position: absolute; left: 22px; top: 18px;
    font-family: "Open Sans", sans-serif;
    font-weight: 700; font-size: 62px; line-height: 1;
    color: var(--wordmark);
    letter-spacing: 4px;
  }
  .brand-tagline {
    position: absolute; left: 24px; top: 95px;
    font-family: "Open Sans", sans-serif;
    font-size: 15px; font-weight: 600;
    letter-spacing: 2.2px;
    color: var(--tag-grey);
    white-space: nowrap;
  }
  .headline {
    position: absolute; right: 14px; top: 30px;
    font-family: "Exo", sans-serif;
    font-weight: 600; font-size: 31px;
    font-variant: small-caps;
    letter-spacing: 1.2px;
    color: var(--white);
    white-space: nowrap;
    text-shadow: 0 1px 2px rgba(0,0,0,0.35);
  }
  .catchphrase {
    position: absolute; right: 20px; top: 80px;
    font-family: "Open Sans", sans-serif;
    font-size: 21px; font-weight: 400;
    letter-spacing: 2px;
    color: var(--white);
    white-space: nowrap;
  }
  .catchphrase strong { font-weight: 800; }
</style>
</head>
<body>
  <div class="banner">
    <svg class="banner-bg" viewBox="0 0 1092 136" preserveAspectRatio="none" aria-hidden="true">
      <polygon points="0,0 276,0 393,136 0,136" fill="var(--panel-white)"/>
    </svg>
    <div class="brand-name">SCEN</div>
    <div class="brand-tagline">INVEST ON YOUR OWN TERMS</div>
    <div class="headline">University Research, Open to Every Investor</div>
    <div class="catchphrase">BEAT THE MARKET. <strong>WITHOUT THE FEES</strong></div>
  </div>
</body>
</html>
```